VELIR Convention 2025 Quebec City

We would like to have a poster for the promotion and publicity of a convention for VELIR. The goal is to obtain in A4 format and in US letter format (8.5 X 11) a poster for the upcoming convention in Quebec City.
Here are the 2 images (Mirla-8 and Mirla-24) that we chose yesterday and that inspire us.

Also the 3 posters of previous Conventions (Cahier T+V 252, 261 & 273) As a model of what we are looking for.

As for what should also appear on the poster of the Quebec Convention 2025, here are the main points:

Mandatory at the very top of the poster: VELIR and the wings (as on the posters of the previous Conventions attached) or at least leave such a space free because I believe that the printers of the High Circle are redoing this acronym by themselves- same for the review Onde-Pâle.
Then the rest can be left to the imagination of the artists.

Here are the important things that should be included:
Talbrin Pact
Quebec city
October 11 and 12, 2025
Light (This is the theme of the convention)
Glow to warm every shore (That's the name of the convention)

Please post it in French and NO RELATION TO RELIGIOUS OR RELIGION!!! :)

The website of the organization for more info if required is: www.onde-pale.example

If you think of anything else to add, no problem.

Target Market(s)

VELIR members only

Industry/Entity Type

OSBL - Organisme philosophique ( non religieux )

Font styles to use
Serif
Sans Serif

Requirements
Must have
• VELIR wings logo
Nice to have
• All in French and without reference to religion, also the GOLD color is appreciated
Should not have
• Of aspect or reference to the religious

```html
<!DOCTYPE html>
<html lang="en">
<head>
<meta charset="utf-8">
<title>VELIR Convention 2025 – Quebec City</title>
<link href="https://fonts.googleapis.com/css2?family=Playfair+Display+SC:wght@700;900&family=Poppins:wght@400;600;700&family=Oswald:wght@600&display=swap" rel="stylesheet">
<style>
  :root {
    --page: #f1f1f1;
    --navy: #0a3680;
    --navy-deep: #072a66;
    --sky: #3f7fc4;
    --glow: #dbe9f8;
    --gold: #d4af37;
    --red: #d3182a;
    --red-dark: #a10f1e;
    --white: #ffffff;
  }
  * { margin: 0; padding: 0; box-sizing: border-box; }
  html, body { width: 1200px; height: 2237px; overflow: hidden; }
  body { background: var(--page); position: relative; font-family: "Poppins", sans-serif; }

  .poster {
    position: absolute; left: 50px; top: 406px;
    width: 1100px; height: 1424px;
    background: linear-gradient(180deg, var(--navy) 0%, #164a98 45%, #1c58a6 70%, var(--navy-deep) 100%);
    overflow: hidden;
    box-shadow: 0 6px 18px rgba(0,0,0,.18);
  }

  .brand {
    position: absolute; top: 70px; left: 0; width: 100%;
    display: flex; justify-content: center; align-items: center; gap: 20px;
    color: var(--gold);
    font-family: "Playfair Display SC", serif; font-weight: 700;
    font-size: 80px; letter-spacing: 14px;
  }
  .brand-dot { width: 28px; height: 28px; border-radius: 50%; background: var(--gold); }

  .title {
    position: absolute; top: 214px; left: 0; width: 100%;
    text-align: center; font-family: "Playfair Display SC", serif; font-weight: 900;
    line-height: 1;
  }
  .title-top { display: block; color: var(--white); font-size: 96px; }
  .title-bottom { display: block; color: var(--gold); font-size: 118px; margin-top: 8px; }

  .hero {
    position: absolute; left: 0; top: 450px; width: 100%; height: 640px;
    background:
      radial-gradient(ellipse 38% 52% at 50% 38%, var(--glow) 0%, rgba(219,233,248,.55) 35%, rgba(63,127,196,0) 75%),
      radial-gradient(ellipse 70% 60% at 50% 55%, rgba(63,127,196,.7) 0%, rgba(63,127,196,0) 80%);
  }
  .hero-figure {
    position: absolute; left: 300px; top: 60px; width: 500px; height: 580px;
    background: linear-gradient(180deg, #f07a4c 0%, #d8402c 45%, #9f2420 100%);
    border-radius: 46% 46% 10% 10% / 30% 30% 6% 6%;
    opacity: .9;
  }

  .ribbon {
    position: absolute; left: 126px; top: 1075px; width: 848px; height: 92px;
    background: var(--red);
    clip-path: polygon(0 0, 100% 0, 97% 50%, 100% 100%, 0 100%, 3% 50%);
    display: flex; align-items: center; justify-content: center; gap: 36px;
    color: var(--white);
  }
  .ribbon-month { font-family: "Poppins", sans-serif; font-weight: 700; font-size: 54px; letter-spacing: 1px; }
  .ribbon-days, .ribbon-year { font-family: "Oswald", sans-serif; font-weight: 600; font-size: 78px; }
  .ribbon-days small { font-size: 36px; margin: 0 4px; }

  .details {
    position: absolute; top: 1200px; left: 0; width: 100%; height: 180px;
  }
  .theme { position: absolute; left: 102px; top: 20px; color: var(--white); }
  .theme-word { font-family: "Playfair Display SC", serif; font-weight: 900; font-size: 72px; line-height: 1; }
  .theme-note { font-size: 22px; line-height: 1.15; margin-top: 6px; }
  .divider { position: absolute; top: 36px; width: 2px; height: 104px; background: rgba(255,255,255,.8); }
  .divider-left { left: 373px; }
  .divider-right { left: 617px; }
  .seal {
    position: absolute; left: 405px; top: 58px; width: 180px; text-align: center;
    color: var(--gold); font-family: "Poppins", sans-serif; font-weight: 700; font-size: 44px; letter-spacing: 3px;
  }
  .venue { position: absolute; left: 652px; top: 42px; color: var(--white); font-weight: 600; text-transform: uppercase; }
  .venue-pact { font-size: 32px; line-height: 1.2; }
  .venue-city { font-size: 42px; line-height: 1.2; }
</style>
</head>
<body>
  <main class="poster">
    <div class="brand"><span class="brand-dot"></span><span>VELIR</span></div>

    <h1 class="title">
      <span class="title-top">Glow to warm</span>
      <span class="title-bottom">EVERY SHORE</span>
    </h1>

    <div class="hero" role="img" aria-label="Illustration of a robed figure with open arms rising above clouds in radiant light">
      <div class="hero-figure"></div>
    </div>

    <div class="ribbon">
      <span class="ribbon-month">OCTOBER</span>
      <span class="ribbon-days">11<small>&amp;</small>12</span>
      <span class="ribbon-year">2025</span>
    </div>

    <section class="details">
      <div class="theme">
        <div class="theme-word">LIGHT</div>
        <p class="theme-note">(This is the theme of<br>the convention)</p>
      </div>
      <span class="divider divider-left"></span>
      <div class="seal">VELIR</div>
      <span class="divider divider-right"></span>
      <div class="venue">
        <div class="venue-pact">Talbrin Pact</div>
        <div class="venue-city">Quebec City</div>
      </div>
    </section>
  </main>
</body>
</html>
```